Baby acupressure app for parents

We need an app for parents that teaches parents how to help them relieve their baby's imbalances (stomach ache, trouble sleeping etc.)

Please see the attached document (with info) and wireframes.

This project is urgent so please only participate if you're able to finish all screens within a few days after the contest is over.

Target Market(s)

Baby moms (20-40 years of age)

Industry/Entity Type

Baby Care

Colors
886aae
b768aa
e667a6
f68d4d
faa54b
fac994
f9ba93
f59195
fee18a

Requirements
Must have
• A high quality design that is both modern and very sleek and stylish.
Nice to have
• Simple animations to make the app "feel" like it's extreme high quality and make the user want to use it again and again
Should not have
• Sandwich menus

```html
<!DOCTYPE html>
<html lang="en">
<head>
<meta charset="utf-8">
<title>Baby Rolig – Problems</title>
<link href="https://fonts.googleapis.com/css2?family=Lato:wght@400;700;900&family=Roboto:wght@400&display=swap" rel="stylesheet">
<style>
  :root {
    --purple: #8a48cf;
    --purple-light: #a24fd8;
    --icon-circle: #8a6aae;
    --icon-shade: #6f5a9c;
    --orange: #faa54b;
    --illustration: #f68d4d;
    --text-dark: #3a3a3a;
    --divider: #dcdcdc;
    --tab-grey: #b0b0b0;
    --white: #ffffff;
  }
  * { box-sizing: border-box; margin: 0; padding: 0; }
  html, body { width: 675px; height: 1200px; overflow: hidden; background: var(--white); }
  body { font-family: "Lato", sans-serif; position: relative; }

  .app-header {
    position: absolute; left: 0; top: 0; width: 675px; height: 136px;
    background: linear-gradient(180deg, var(--purple) 0%, var(--purple-light) 100%);
    color: var(--white);
  }
  .status-bar {
    position: absolute; top: 8px; left: 16px; right: 14px; height: 30px;
    display: flex; align-items: center; justify-content: space-between;
    font-family: "Roboto", sans-serif; font-size: 20px;
  }
  .status-left, .status-right { display: flex; align-items: center; gap: 8px; }
  .app-title {
    position: absolute; top: 64px; width: 100%; text-align: center;
    font-weight: 900; font-size: 31px; letter-spacing: 1.5px;
  }

  .hero {
    position: absolute; left: 0; top: 136px; width: 675px; height: 264px;
    background: var(--orange); color: var(--white);
  }
  .hero-title {
    position: absolute; left: 51px; top: 42px;
    font-weight: 900; font-size: 32px; letter-spacing: 1.5px;
  }
  .hero-rule { position: absolute; left: 51px; top: 92px; width: 108px; height: 1px; background: var(--white); }
  .hero-text {
    position: absolute; left: 51px; top: 106px; width: 336px;
    font-size: 13px; line-height: 21.6px;
  }
  .hero-illustration {
    position: absolute; left: 398px; top: 8px; width: 232px; height: 256px;
    background: linear-gradient(160deg, #f9ba93 0%, var(--illustration) 60%, #e667a6 100%);
    border-radius: 80px 80px 0 0;
  }

  .problem-list { position: absolute; left: 0; top: 400px; width: 675px; list-style: none; }
  .problem-row {
    position: relative; height: 135px; border-bottom: 1px solid var(--divider);
    display: flex; align-items: center; background: var(--white);
  }
  .problem-row:last-child { height: 142px; border-bottom: none; }
  .problem-row.is-active {
    background: var(--purple); border-bottom: none;
    box-shadow: 0 -4px 10px rgba(0,0,0,.12), 0 4px 10px rgba(0,0,0,.12);
  }
  .problem-icon {
    position: absolute; left: 29px; width: 88px; height: 88px; border-radius: 50%;
    background: linear-gradient(135deg, var(--icon-circle) 50%, var(--icon-shade) 50%);
  }
  .problem-label {
    position: absolute; left: 141px;
    font-weight: 700; font-size: 16px; color: var(--text-dark); letter-spacing: .2px;
  }
  .is-active .problem-label { color: var(--white); }
  .chevron { position: absolute; left: 620px; width: 26px; height: 46px; }

  .tab-bar {
    position: absolute; left: 0; top: 1085px; width: 675px; height: 115px;
    background: var(--white); border-top: 1px solid var(--divider);
  }
  .tab {
    position: absolute; top: 0; width: 110px; height: 115px;
    display: flex; flex-direction: column; align-items: center;
    font-family: "Roboto", sans-serif; font-size: 17px; color: var(--tab-grey);
  }
  .tab svg { margin-top: 28px; margin-bottom: 8px; }
  .tab.is-current { color: var(--purple); }
  .fab {
    position: absolute; left: 286px; top: -17px; width: 108px; height: 108px; border-radius: 50%;
    background: linear-gradient(180deg, var(--purple) 0%, var(--purple-light) 100%);
    box-shadow: 0 6px 16px rgba(138,72,207,.35);
    display: flex; align-items: center; justify-content: center;
  }
</style>
</head>
<body>
  <header class="app-header">
    <div class="status-bar">
      <div class="status-left">
        <svg width="68" height="14" viewBox="0 0 68 14" fill="#fff">
          <circle cx="7" cy="7" r="6"/><circle cx="20" cy="7" r="6"/><circle cx="33" cy="7" r="6"/><circle cx="46" cy="7" r="6"/>
          <circle cx="59" cy="7" r="5.3" fill="none" stroke="#fff" stroke-width="1.4"/>
        </svg>
        <span>Carrier</span>
        <svg width="20" height="16" viewBox="0 0 20 16" fill="none" stroke="#fff" stroke-width="2.2" stroke-linecap="round">
          <path d="M2 6a12 12 0 0 1 16 0"/><path d="M5 9.5a7.5 7.5 0 0 1 10 0"/><circle cx="10" cy="13" r="1.2" fill="#fff"/>
        </svg>
      </div>
      <div class="status-right">
        <svg width="20" height="20" viewBox="0 0 20 20" fill="none" stroke="#fff" stroke-width="1.6">
          <path d="M16 6a8 8 0 1 0 1.5 6"/><rect x="7" y="9" width="6" height="5" fill="#fff"/><path d="M8 9V7.5a2 2 0 0 1 4 0V9"/>
        </svg>
        <span>100%</span>
        <svg width="46" height="20" viewBox="0 0 46 20">
          <rect x="1" y="2" width="40" height="16" rx="3" fill="none" stroke="#fff" stroke-width="1.6"/>
          <rect x="3.5" y="4.5" width="35" height="11" rx="1.5" fill="#fff"/>
          <rect x="42.5" y="7" width="2.5" height="6" rx="1" fill="#fff"/>
        </svg>
      </div>
    </div>
    <h1 class="app-title">BABY ROLIG</h1>
  </header>

  <section class="hero">
    <h2 class="hero-title">PROBLEMS</h2>
    <div class="hero-rule"></div>
    <p class="hero-text">Lorem Ipsum is simply dummy text of the printing and typesetting industry. Lorem Ipsum has been the indus­try's standard dummy text ever since the 1500s, when an unknown printer took a galley of type and scrambled it to make a type specimen book</p>
    <div class="hero-illustration" role="img" aria-label="Illustration of a mother holding her baby"></div>
  </section>

  <ul class="problem-list">
    <li class="problem-row">
      <div class="problem-icon" role="img" aria-label="Stomach icon"></div>
      <span class="problem-label">STOMACH ACHE</span>
      <svg class="chevron" viewBox="0 0 26 46" fill="none" stroke="#444" stroke-width="2.6"><path d="M2 2l21 21L2 44"/></svg>
    </li>
    <li class="problem-row">
      <div class="problem-icon" role="img" aria-label="Bed icon"></div>
      <span class="problem-label">BAD SLEEP</span>
      <svg class="chevron" viewBox="0 0 26 46" fill="none" stroke="#444" stroke-width="2.6"><path d="M2 2l21 21L2 44"/></svg>
    </li>
    <li class="problem-row">
      <div class="problem-icon" role="img" aria-label="Coughing head icon"></div>
      <span class="problem-label">COLD, COUGHING</span>
      <svg class="chevron" viewBox="0 0 26 46" fill="none" stroke="#444" stroke-width="2.6"><path d="M2 2l21 21L2 44"/></svg>
    </li>
    <li class="problem-row is-active">
      <div class="problem-icon" role="img" aria-label="Ear icon"></div>
      <span class="problem-label">EAR PAIN</span>
      <svg class="chevron" viewBox="0 0 26 46" fill="none" stroke="#fff" stroke-width="2.6"><path d="M2 2l21 21L2 44"/></svg>
    </li>
    <li class="problem-row">
      <div class="problem-icon" role="img" aria-label="Hand icon"></div>
      <span class="problem-label">ECZEMA</span>
      <svg class="chevron" viewBox="0 0 26 46" fill="none" stroke="#444" stroke-width="2.6"><path d="M2 2l21 21L2 44"/></svg>
    </li>
  </ul>

  <nav class="tab-bar">
    <div class="tab" style="left:31px">
      <svg width="40" height="36" viewBox="0 0 40 36" fill="none" stroke="#b0b0b0" stroke-width="2"><path d="M2 17L20 2l18 15"/><path d="M7 13v21h9V22h8v12h9V13"/></svg>
      <span>Home</span>
    </div>
    <div class="tab is-current" style="left:152px">
      <svg width="36" height="36" viewBox="0 0 36 36" fill="none" stroke="#8a48cf" stroke-width="3"><circle cx="18" cy="11" r="6"/><path d="M5 33v-4c0-4 4-7 13-7s13 3 13 7v4z"/></svg>
      <span>Problems</span>
    </div>
    <div class="fab">
      <svg width="30" height="30" viewBox="0 0 30 30" stroke="#fff" stroke-width="3.2"><path d="M15 2v26M2 15h26"/></svg>
    </div>
    <div class="tab" style="left:412px">
      <svg width="40" height="40" viewBox="0 0 40 40" fill="none" stroke="#b0b0b0" stroke-width="2"><circle cx="31" cy="8" r="5.5"/><circle cx="9" cy="20" r="5.5"/><circle cx="31" cy="32" r="5.5"/><path d="M14 17.5l12-7M14 22.5l12 7"/></svg>
      <span>Share</span>
    </div>
    <div class="tab" style="left:544px">
      <svg width="24" height="44" viewBox="0 0 24 44" fill="#b0b0b0"><circle cx="14" cy="6" r="5.5"/><path d="M8 16h10l-4 22h5l-1 4H5l1-4h3l3-18H7z"/></svg>
      <span>About</span>
    </div>
  </nav>
</body>
</html>
```